New website

Our website (www.larchvale.com) needs to be replaced with something gorgeous and glossy. We do like the text of our current website but have many new images to put on the site. We want to create a website that shows viewers what our team can do, and how we can create something amazing for them and their homes.

Coding

```html
<!DOCTYPE html>
<html lang="en">
<head>
<meta charset="utf-8">
<title>Larchvale Landscaping</title>
<link rel="stylesheet" href="https://fonts.googleapis.com/css2?family=Cinzel:wght@400;600&family=Lora:wght@500&family=Roboto:wght@300;400&display=swap">
<style>
:root{
  --green:#46b863;
  --green-dark:#3aa555;
  --blue:#2b80c6;
  --ink:#222;
  --muted:#555;
  --grey-bg:#f1f1f1;
  --white:#fff;
}
*{box-sizing:border-box;margin:0;padding:0}
html,body{width:1200px;height:3482px;overflow:hidden}
body{position:relative;background:var(--white);font-family:"Roboto",sans-serif;color:var(--ink)}
.abs{position:absolute}
.serif{font-family:"Cinzel",serif}
.btn{position:absolute;display:flex;align-items:center;justify-content:center;background:var(--blue);color:var(--white);font-family:"Cinzel",serif;font-weight:600;font-size:15px;letter-spacing:.5px}
.accent{color:var(--green)}

/* top bar */
.topbar{left:0;top:0;width:1200px;height:40px;background:var(--green);color:var(--white);font-size:13px}
.topbar .info{position:absolute;top:12px;display:flex;align-items:center;gap:5px}
.topbar .sep{position:absolute;top:9px;width:1px;height:22px;background:rgba(255,255,255,.5)}

/* nav */
.logo{font-family:"Cinzel",serif;font-size:30px;letter-spacing:5px;color:#3a4a5a;display:flex;align-items:center;gap:10px}
.logo .dot{width:14px;height:14px;border-radius:50%;background:var(--blue)}
.nav a{position:absolute;top:72px;font-size:14.5px;color:var(--ink);text-decoration:none}
.nav a.current{color:var(--green);text-decoration:underline}

/* hero */
.hero{left:0;top:119px;width:1200px;height:620px;background:linear-gradient(100deg,#3b3d3c 0%,#5c6452 30%,#4e7a3b 55%,#3d6b2c 80%,#5b8f3a 100%)}
.hero-title{left:104px;color:var(--white);line-height:1}
.hero-text{left:104px;top:452px;width:360px;color:var(--white);font-size:14px;line-height:24px}

/* about */
.photo-circle{left:136px;top:824px;width:392px;height:392px;border-radius:50%;background:radial-gradient(circle at 40% 45%,#7fae3a,#4b7a24 60%,#2d4c18)}
.ring{left:126px;top:814px;width:412px;height:412px;border-radius:50%;border:6px solid transparent;background:linear-gradient(135deg,#2b80c6,#9cc4e4 70%,#e8eef4) border-box;-webkit-mask:linear-gradient(#000 0 0) padding-box,linear-gradient(#000 0 0);-webkit-mask-composite:xor;mask-composite:exclude}
.eyebrow{font-family:"Cinzel",serif;font-size:22px;color:var(--ink)}
.section-title{font-family:"Cinzel",serif;font-size:31px;font-weight:600;color:#333;line-height:40px}
.about-title{font-size:26px;line-height:40px;white-space:nowrap}
.body-text{font-size:14px;line-height:22.5px;color:var(--muted);font-weight:300}

/* services */
.services{left:0;top:1324px;width:1200px;height:756px;background:var(--grey-bg)}
.card{position:absolute;top:1567px;width:322px;height:341px;background:var(--white);border-radius:12px;overflow:hidden}
.card .img{position:absolute;left:0;top:0;width:322px;height:205px}
.card .icon{position:absolute;left:116px;top:160px;width:90px;height:90px;border-radius:50%;background:var(--blue);border:3px solid var(--white);display:flex;align-items:center;justify-content:center}
.card h3{position:absolute;left:0;top:255px;width:322px;text-align:center;font-family:"Lora",serif;font-weight:500;font-size:20px;line-height:28px;color:var(--blue)}
.card.active{background:var(--green)}
.card.active h3{color:var(--white)}
.card.active .icon{background:var(--green)}

.center{left:0;width:1200px;text-align:center}

/* footer */
.foot-head{font-family:"Cinzel",serif;font-weight:600;font-size:17px;color:#333}
.foot-list{font-size:14px;color:var(--ink);line-height:29px;list-style:none}
</style>
</head>
<body>

<!-- top bar -->
<div class="abs topbar">
  <div class="info" style="left:105px">
    <svg width="9" height="13" viewBox="0 0 9 13"><path d="M4.5 0A4.5 4.5 0 0 0 0 4.5C0 8 4.5 13 4.5 13S9 8 9 4.5A4.5 4.5 0 0 0 4.5 0zm0 6.3a1.8 1.8 0 1 1 0-3.6 1.8 1.8 0 0 1 0 3.6z" fill="#fff"/></svg>
    Cedar Hollow, MI 49012
  </div>
  <div class="sep" style="left:274px"></div>
  <div class="info" style="left:289px">
    <svg width="12" height="12" viewBox="0 0 24 24"><path d="M6.6 10.8a15 15 0 0 0 6.6 6.6l2.2-2.2a1 1 0 0 1 1-.25 11.4 11.4 0 0 0 3.6.57 1 1 0 0 1 1 1V20a1 1 0 0 1-1 1A17 17 0 0 1 3 4a1 1 0 0 1 1-1h3.5a1 1 0 0 1 1 1 11.4 11.4 0 0 0 .57 3.6 1 1 0 0 1-.25 1z" fill="#fff"/></svg>
    (555) 214-7730
  </div>
  <div class="sep" style="left:408px"></div>
  <div class="info" style="left:423px">
    <svg width="12" height="12" viewBox="0 0 12 12"><circle cx="6" cy="6" r="5" fill="none" stroke="#fff" stroke-width="1.4"/><path d="M6 3v3.2l2 1.2" fill="none" stroke="#fff" stroke-width="1.3"/></svg>
    Mon-Sat: 7:00am-7:00pm
  </div>
  <div class="btn" style="left:815px;top:0;width:280px;height:40px;font-size:14px">Schedule An Appointment</div>
</div>

<!-- nav -->
<div class="abs logo" style="left:105px;top:62px"><span class="dot"></span>LARCHVALE</div>
<nav class="nav">
  <a class="current" style="left:505px">Home</a>
  <a style="left:573px">About Us</a>
  <a style="left:660px">Services ⌄</a>
  <a style="left:755px">Testimonials</a>
  <a style="left:866px">Contact Us ⌄</a>
</nav>
<div class="btn" style="left:984px;top:58px;width:111px;height:40px">Log In</div>

<!-- hero -->
<div class="abs hero" role="img" aria-label="Stone-and-timber house with a paved driveway, lush lawn and landscaped garden beds"></div>
<svg class="abs" style="left:0;top:620px" width="1200" height="120" viewBox="0 0 1200 120">
  <defs><linearGradient id="wave" x1="0" x2="1"><stop offset="0" stop-color="#2b80c6"/><stop offset=".6" stop-color="#5ea3d8"/><stop offset="1" stop-color="#d6e8f5"/></linearGradient></defs>
  <path d="M0 55 C250 120 520 120 800 60 C950 28 1080 20 1200 52 L1200 120 L0 120Z" fill="url(#wave)"/>
  <path d="M0 62 C250 110 520 108 800 70 C950 48 1080 42 1200 60 L1200 120 L0 120Z" fill="#fff"/>
</svg>
<div class="abs hero-title serif" style="top:318px;font-size:46px">Welcome To</div>
<div class="abs hero-title serif" style="top:372px;font-size:66px;font-weight:600">Larchvale</div>
<p class="abs hero-text">While the scope of our landscaping company has grown, our way of doing business has not.</p>
<div class="btn" style="left:107px;top:513px;width:279px;height:40px">Schedule An Appointment</div>

<!-- about -->
<div class="abs ring"></div>
<div class="abs photo-circle" role="img" aria-label="Landscaper pushing a lawn mower across a green garden lawn"></div>
<div class="abs eyebrow" style="left:638px;top:832px">About Us</div>
<h2 class="abs section-title about-title" style="left:636px;top:866px">More Than Just <span class="accent">Landscaping</span><br><span class="accent">&amp; Snow Removal</span></h2>
<p class="abs body-text" style="left:637px;top:955px;width:440px">Established in 2005 as a way to pay for college tuition, Larchvale has instead become our passion. With a garage sale mower and a commitment to doing every job well, our list of satisfied customers grew quickly over the years.</p>
<p class="abs body-text" style="left:637px;top:1055px;width:440px">While the scope of our landscaping company has grown, our way of doing business has not. It is still rooted in the desire to do quality work whether the job includes a simple tree service or the installation of an entire irrigation system,</p>
<div class="btn" style="left:637px;top:1162px;width:158px;height:40px">Read More</div>

<!-- services -->
<div class="abs services"></div>
<div class="abs center eyebrow" style="top:1426px">Our Services</div>
<h2 class="abs center section-title" style="top:1460px;font-size:32px">What <span class="accent">We Do</span></h2>

<div class="card" style="left:104px">
  <div class="img" role="img" aria-label="Orange lawn mower cutting grass in a sunny yard" style="background:linear-gradient(180deg,#8aa85a,#6f9a3a 55%,#5a8a2c)"></div>
  <div class="icon"><svg width="40" height="34" viewBox="0 0 40 34"><path d="M4 2l8 14" stroke="#fff" stroke-width="2.5" fill="none"/><rect x="8" y="15" width="22" height="10" rx="3" fill="#fff"/><circle cx="12" cy="28" r="4" fill="#fff"/><circle cx="30" cy="28" r="4" fill="#fff"/></svg></div>
  <h3>Lawn Maintenance</h3>
</div>
<div class="card active" style="left:439px">
  <div class="img" role="img" aria-label="Garden lamp post and sprinkler watering colourful flower beds" style="background:linear-gradient(180deg,#b9c8b4,#7f9d68 55%,#5d8a45)"></div>
  <div class="icon"><svg width="42" height="38" viewBox="0 0 42 38"><path d="M21 14v20M21 34c-6-6-12-6-14-2M21 34c6-6 12-6 14-2" stroke="#fff" stroke-width="2.4" fill="none"/><path d="M21 14l-8-8M21 14l8-8M21 14V3" stroke="#fff" stroke-width="1.6" stroke-dasharray="2 3" fill="none"/></svg></div>
  <h3 style="top:242px">Irrigation Installation &amp;<br>Maintenance</h3>
</div>
<div class="card" style="left:774px">
  <div class="img" role="img" aria-label="Gardener trimming shrubs with hedge shears" style="background:linear-gradient(180deg,#a8b86a,#6f9a3a 55%,#4f7e2a)"></div>
  <div class="icon"><svg width="36" height="38" viewBox="0 0 36 38"><circle cx="11" cy="7" r="4" fill="#fff"/><path d="M6 14h10l6 6-3 3-4-4v17H6z" fill="#fff"/><rect x="20" y="22" width="14" height="14" fill="#fff"/></svg></div>
  <h3>Landscape Maintenance</h3>
</div>

<svg class="abs" style="left:577px;top:1975px" width="46" height="20" viewBox="0 0 46 20">
  <circle cx="10" cy="10" r="9" fill="#111"/><path d="M12 5l-5 5 5 5" stroke="#fff" stroke-width="2.2" fill="none"/>
  <circle cx="36" cy="10" r="9" fill="#46b863"/><path d="M34 5l5 5-5 5" stroke="#fff" stroke-width="2.2" fill="none"/>
</svg>

<!-- why choose us -->
<div class="abs" role="img" aria-label="Aerial view of a worker mowing a wide green lawn" style="left:0;top:2290px;width:1200px;height:560px;background:linear-gradient(180deg,#fff 0%,#b7cfa2 18%,#6f9a4e 45%,#557f3a 100%)"></div>
<div class="abs center eyebrow" style="top:2153px">Larchvale</div>
<h2 class="abs center section-title" style="top:2187px;font-size:32px">Why <span class="accent">Choose Us?</span></h2>
<p class="abs" style="left:145px;top:2243px;width:910px;text-align:center;font-size:14px;line-height:22.5px;color:var(--ink)">You shouldn't have to spend hours on grounds maintenance to enjoy a well-designed and well-maintained yard. The landscaping professionals at Larchvale can handle your landscape maintenance, so you can focus on the demands of your family, job, and more.We're top rated landscapers; our passion for the work we do is what makes us a clear leader among other landscaping companies in the area. When you are a part of our Lawn Maintenance program, we provide regularly-scheduled maintenance visits.</p>
<div class="btn" style="left:520px;top:2358px;width:159px;height:40px">Read More</div>

<svg class="abs" style="left:0;top:2690px" width="1200" height="472" viewBox="0 0 1200 472">
  <path d="M0 20 C180 80 330 110 520 80 C720 48 840 0 1000 20 C1090 32 1150 60 1200 78 L1200 472 L0 472Z" fill="#44ad5c"/>
  <path d="M0 30 C180 88 330 118 520 88 C720 56 840 8 1000 28 C1090 40 1150 68 1200 86 L1200 472 L0 472Z" fill="#46b863"/>
</svg>
<div class="abs center" style="top:2864px;font-family:'Lora',serif;font-size:22px;color:#fff">Get In Touch</div>
<h2 class="abs center section-title" style="top:2898px;font-size:32px;color:#fff">Contact Us Today</h2>
<p class="abs" style="left:220px;top:2962px;width:760px;text-align:center;font-size:15px;line-height:24px;color:#fff">We're top rated landscapers; our passion for the work we do is what makes us a clear leader among other landscaping companies in the area.</p>
<div class="btn" style="left:512px;top:3030px;width:176px;height:40px">Get Started</div>

<!-- footer -->
<div class="abs logo" style="left:105px;top:3262px"><span class="dot"></span>LARCHVALE</div>
<div class="abs foot-head" style="left:450px;top:3235px">Quick Links</div>
<ul class="abs foot-list" style="left:452px;top:3262px">
  <li>Home</li><li>About Us</li><li>Services</li><li>Testimonials</li><li>Contact Us</li>
</ul>
<div class="abs foot-head" style="left:643px;top:3235px">Help Links</div>
<ul class="abs foot-list" style="left:645px;top:3262px">
  <li>Blog</li><li>Contact</li><li>Privacy Policy</li>
</ul>
<div class="abs foot-head" style="left:805px;top:3235px">Contact Us</div>
<div class="abs" style="left:807px;top:3270px;font-size:14px;line-height:22.5px">1820 Birchmoor Lane NE<br>Cedar Hollow, MI 49012</div>
<div class="abs" style="left:807px;top:3323px;font-size:14px">(555) 214-7730</div>
<div class="abs" style="left:807px;top:3358px;font-size:14px;line-height:22.5px">Monday-Saturday: 7:00am-7:00pm<br>Closed Sunday</div>
<div class="abs" style="left:105px;top:3434px;width:990px;height:1px;background:linear-gradient(90deg,transparent,#bbb 20%,#bbb 80%,transparent)"></div>
<div class="abs center" style="top:3453px;font-size:12px;color:#333">©2025 Larchvale Landscaping - All rights reserved.</div>

</body>
</html>
```